Etiketten-Design für Eierschachtel
Zielgruppe
Wir haben einen Hofladen, indem wir unsere hofeigenen Produkte direkt an den Verbraucher verkaufen.
Aufgabenstellung
Wir suchen ein Etikett für unsere Eierschachtel, die wir für den Verkauf unserer Eier im eigenen Hofladen benötigen.
Das Etikett soll hell und freundlich, aber keinesfalls überladen oder zu verspielt sein. Es soll die Natürlichkeit und Regionalität widerspiegeln. Wir halten unsere Hühner in mobiler Freilandhaltung mit ausreichend Auslauf auf unseren Wiesen.
Das beigefügte Logo (einmal farbig, einmal schwarz/weiß - je nach Vorschlag was besser passt) soll integriert werden.
Das Etikett soll folgende Punkte enthalten:
Rückseite:
- 'Verbraucherhinweis: Nach dem Kauf bei Kühlschranktemperatur aufbewahren. Nach Ablauf des
Mindesthaltbarkeitsdatums durcherhitzen.'
- Familie Lohwanger
Tannweg 27
74912 Kellinghofen
Vorderseite (zum Öffnen der Eierschachtel) bzw. Deckel oben:
- '10 frische Eier aus mobiler Freilandhaltung' (gerne auch eigene Vorschläge von Ihnen)
- passender Slogan, der auf Regionalität bzw. Einkaufen direkt beim Erzeuger basiert
Format: ca. 21,4cm breit und ca. 14,2cm lang

```html
<!DOCTYPE html>
<html lang="de">
<head>
<meta charset="utf-8">
<title>Eierschachtel-Etikett – Lohwanger Hof</title>
<link href="https://fonts.googleapis.com/css2?family=Open+Sans:wght@400;600;700;800&display=swap" rel="stylesheet">
<style>
  :root{
    --page:#ffffff;
    --mint:#ecf1ea;
    --cream:#f2e4d8;
    --info-green:#5a9e52;
    --brand-green:#2f8a2a;
    --rust:#7a2e0e;
    --caramel:#a97a52;
    --egg:#f4efe8;
  }
  *{margin:0;padding:0;box-sizing:border-box}
  html,body{width:1200px;height:2174px;overflow:hidden;background:var(--page)}
  body{position:relative;font-family:"Open Sans",sans-serif}
  .label{
    position:absolute;left:60px;top:801px;width:1008px;height:534px;
    transform:scale(1.0714);transform-origin:0 0;
  }
  .back-strip{
    position:absolute;left:0;top:0;width:1008px;height:95px;background:var(--mint);
    transform:rotate(180deg);color:var(--info-green);
  }
  .back-strip .block{position:absolute;top:8px;font-size:10px;line-height:13px}
  .back-strip .block strong{display:block;font-size:12.5px;font-weight:600;line-height:17px}
  .address{left:96px}
  .notice{left:669px}
  .hero{
    position:absolute;left:0;top:95px;width:1008px;height:344px;overflow:hidden;
    background:linear-gradient(90deg,#cfcfc9 0%,#b9bcb0 22%,#8fa56a 45%,#5f8a3c 70%,#7fa84e 100%);
  }
  .hero .hen{
    position:absolute;left:555px;top:55px;width:230px;height:289px;
    border-radius:45% 50% 10% 30%;
    background:radial-gradient(ellipse at 45% 40%,#b76a2a,#8a4514 75%);
    opacity:.9;
  }
  .brand{position:absolute;left:75px;top:95px;width:210px;text-align:center}
  .brand .ring{width:100px;height:100px;margin:0 auto 6px;border:2px solid var(--brand-green);border-radius:50%}
  .brand .name{font-size:25px;font-weight:600;color:var(--brand-green);letter-spacing:.5px}
  .title{
    position:absolute;left:282px;top:117px;width:356px;height:71px;background:var(--rust);
    color:#fff;padding:5px 0 0 17px;
  }
  .title h1{font-size:34px;font-weight:700;line-height:38px}
  .title p{font-size:16.5px;font-weight:400;line-height:18px}
  .count{
    position:absolute;left:786px;top:242px;width:90px;height:130px;
    border-radius:50% 50% 50% 50%/60% 60% 40% 40%;background:var(--egg);
    text-align:center;color:var(--rust);padding-top:28px;
  }
  .count b{display:block;font-size:50px;font-weight:800;line-height:50px}
  .count span{display:block;font-size:10px;font-weight:700;margin-top:2px}
  .slogan{
    position:absolute;left:0;top:439px;width:1008px;height:95px;background:var(--cream);
    text-align:center;color:var(--caramel);padding-top:20px;
  }
  .slogan small{display:block;font-size:19px;font-weight:700;line-height:24px}
  .slogan strong{display:block;font-size:33px;font-weight:700;line-height:38px}
</style>
</head>
<body>
  <section class="label">
    <div class="back-strip">
      <div class="block address">
        <strong>Familie Lohwanger</strong>
        Tannweg 27<br>74912 Kellinghofen
      </div>
      <div class="block notice">
        <strong>Verbraucherhinweis:</strong>
        Nach dem Kauf bei Kühlschranktemperatur aufbewahren.<br>
        Nach Ablauf des Mindesthaltbarkeitsdatums durcherhitzen.
      </div>
    </div>
    <div class="hero" role="img" aria-label="Foto: braunes Huhn auf einer grünen Wiese mit unscharfem Weg im Hintergrund">
      <div class="hen"></div>
    </div>
    <div class="brand">
      <div class="ring"></div>
      <div class="name">LOHWANGER HOF</div>
    </div>
    <div class="title">
      <h1>FRISCHE EIER AUS</h1>
      <p>MOBILER FREILANDHALTUNG</p>
    </div>
    <div class="count"><b>10</b><span>FRISCHE EIER</span></div>
    <div class="slogan">
      <small>Weil's aus der</small>
      <strong>Region am besten ist</strong>
    </div>
  </section>
</body>
</html>
```